Dufresne Roofing

Want a professional looking business card

Industry/Entity Type

Business

Contact Information for Business Card

Marc Dufresne ( Owner) marc@dufresneroofing-example.com, www.dufresneroofing-example.com, Adress: 4217 County road 42 Wendover,ON K0A3M1

```html
<!DOCTYPE html>
<html lang="en">
<head>
<meta charset="utf-8">
<title>Dufresne Roofing – Business Card</title>
<link href="https://fonts.googleapis.com/css2?family=Open+Sans:ital,wght@0,400;0,600;0,700;1,400&family=Roboto:wght@500&display=swap" rel="stylesheet">
<style>
  :root {
    --brand-blue: #1d4488;
    --ink-grey: #4a4a4a;
    --soft-grey: #7a7a7a;
    --card-white: #ffffff;
    --backdrop: #d6d6d6;
  }
  * { box-sizing: border-box; margin: 0; padding: 0; }
  html, body {
    width: 1200px; height: 900px; overflow: hidden;
    background: var(--backdrop);
    font-family: "Open Sans", Arial, sans-serif;
  }
  .canvas {
    width: 1200px; height: 900px;
    display: flex; flex-direction: column; align-items: center; justify-content: center;
    gap: 36px;
  }
  .card {
    width: 700px; height: 400px;
    background: var(--card-white);
    position: relative;
    box-shadow: 0 6px 18px rgba(0,0,0,0.18);
  }
  /* Front side */
  .card-front .brand-name {
    position: absolute; left: 0; right: 0; top: 150px;
    text-align: center;
    font-weight: 700; font-size: 46px; letter-spacing: 3px;
    color: var(--brand-blue); text-transform: uppercase;
  }
  .card-front .site {
    position: absolute; right: 46px; bottom: 34px;
    font-size: 15px; letter-spacing: 0.5px; color: var(--ink-grey);
  }
  /* Back side */
  .card-back .brand-name {
    position: absolute; left: 0; right: 0; top: 52px;
    text-align: center;
    font-weight: 700; font-size: 44px; letter-spacing: 3px;
    color: var(--brand-blue); text-transform: uppercase;
  }
  .identity {
    position: absolute; right: 390px; top: 200px;
    text-align: right;
  }
  .identity .person {
    font-family: "Roboto", Arial, sans-serif; font-weight: 500;
    font-size: 27px; color: var(--brand-blue);
  }
  .identity .role {
    font-style: italic; font-size: 21px; color: var(--soft-grey);
  }
  .divider {
    position: absolute; left: 330px; top: 200px;
    width: 2px; height: 64px; background: var(--brand-blue);
  }
  .contacts {
    position: absolute; left: 352px; top: 198px;
    list-style: none;
  }
  .contacts li {
    display: flex; align-items: center; gap: 12px;
    font-size: 16px; letter-spacing: 0.6px; color: var(--ink-grey);
    height: 23px;
  }
  .contacts svg { width: 14px; height: 14px; flex: none; }
  .address {
    position: absolute; left: 60px; bottom: 44px;
    display: flex; align-items: center; gap: 12px;
    font-size: 17px; letter-spacing: 0.6px; color: var(--ink-grey);
  }
  .address svg { width: 18px; height: 18px; }
</style>
</head>
<body>
<main class="canvas">
  <section class="card card-front">
    <div class="brand-name">Dufresne Roofing</div>
    <div class="site">www.dufresneroofing-example.com</div>
  </section>

  <section class="card card-back">
    <div class="brand-name">Dufresne Roofing</div>

    <div class="identity">
      <div class="person">Marc Dufresne</div>
      <div class="role">Owner</div>
    </div>
    <div class="divider"></div>

    <ul class="contacts">
      <li>
        <svg viewBox="0 0 14 14" aria-hidden="true"><rect x="3.5" y="1" width="7" height="12" rx="1.2" fill="none" stroke="var(--brand-blue)" stroke-width="1.5"/><circle cx="7" cy="11" r="0.8" fill="var(--brand-blue)"/></svg>
        <span>(000)123-4567</span>
      </li>
      <li>
        <svg viewBox="0 0 14 14" aria-hidden="true"><rect x="1" y="3" width="12" height="8.5" fill="var(--brand-blue)"/><path d="M1 3 L7 8 L13 3" fill="none" stroke="#fff" stroke-width="1.2"/></svg>
        <span>marc@dufresneroofing-example.com</span>
      </li>
      <li>
        <svg viewBox="0 0 14 14" aria-hidden="true"><circle cx="6" cy="6" r="4" fill="none" stroke="var(--brand-blue)" stroke-width="2"/><path d="M9 9 L13 13" stroke="var(--brand-blue)" stroke-width="2.4" stroke-linecap="round"/></svg>
        <span>www.dufresneroofing-example.com</span>
      </li>
    </ul>

    <div class="address">
      <svg viewBox="0 0 18 18" aria-hidden="true"><path d="M17 1 L1 8 L8 10 L10 17 Z" fill="var(--brand-blue)"/></svg>
      <span>4217 County road 42 Wendover,ON K0A3M1</span>
    </div>
  </section>
</main>
</body>
</html>
```